Calm Fern Healthcare- Aged Care and Community Services

Looking for brochure to advertise our services. I will attach a draft that we do not want to use. Looking for graphics that are as natural as possible to present a personalised service. We supply services to aged people and people with disability. Please make it look classy and professional at the same time. I am looking for creativity. I have also attached the logo. Site addresses can be the last page. ideally looking for 2 designs, one A4 and another smaller possibly DL. Looking for creative out of the box thinkers. Thank you.

Target Market(s)

Aged Care service providers, disability service providers and private hospitals

Font styles to use
Serif
Sans Serif
Script

Colors
6b449b
886aae
eea4c8
f59195
fac994
3176b5
0555a3
cedeed
e4daeb

Requirements
Must have
• Targeted imagery, content and contact details
Nice to have
• personal profiles of people happy with our services

```html
<!DOCTYPE html>
<html lang="en">
<head>
<meta charset="utf-8">
<title>Calm Fern Healthcare – Tri-fold Brochure</title>
<link rel="stylesheet" href="https://fonts.googleapis.com/css2?family=Lato:wght@300;400;700;900&family=Open+Sans:ital,wght@0,400;0,600;0,700;1,400&display=swap">
<style>
  :root{
    --purple:#6a2c91;
    --purple-deep:#5a2380;
    --pink:#e5287d;
    --lilac:#8a63b0;
    --blue:#2f7fc1;
    --teal:#1fa7a0;
    --green:#4cae4f;
    --ink:#3b3340;
    --grey:#6f6a74;
    --paper:#ffffff;
    --panel-tint:#f4f3f6;
    --stage:#e6e5ea;
  }
  *{box-sizing:border-box;margin:0;padding:0}
  html,body{width:1200px;height:2400px;overflow:hidden;background:var(--stage)}
  body{position:relative;font-family:'Open Sans',Arial,sans-serif;color:var(--ink)}

  .spread{position:absolute;left:60px;width:1080px;height:764px;background:var(--paper);
    box-shadow:0 10px 30px rgba(40,20,60,.18);overflow:hidden}
  .spread--outside{top:318px}
  .spread--inside{top:1318px}
  .layer{position:absolute;left:0;top:0;width:1080px;height:764px}

  .block{position:absolute}
  .heading{font-family:'Lato',Arial,sans-serif;font-size:17px;color:var(--purple);
    text-transform:uppercase;letter-spacing:.3px;line-height:1.1}
  .heading b{font-weight:900;position:relative}
  .heading b::after{content:"";position:absolute;left:0;bottom:-5px;width:30px;height:3px;background:var(--pink)}
  .heading span{font-weight:300}
  .body-copy{font-size:8px;line-height:1.5;color:var(--grey);margin-top:12px}
  .body-copy + .body-copy{margin-top:6px}

  .value-list{list-style:none;margin-top:14px}
  .value-list li{display:flex;gap:8px;align-items:flex-start;font-size:8px;line-height:1.4;color:var(--grey);margin-bottom:7px}
  .value-list .num{font-family:'Lato',Arial,sans-serif;font-weight:300;color:var(--pink);font-size:14px;line-height:1;flex:0 0 auto}
  .value-list--pair{display:grid;grid-template-columns:1fr 1fr;column-gap:14px}
  .value-list--pair li{font-size:7px}
  .value-list--pair .num{font-size:11px}

  .hours{color:#fff;text-align:center}
  .hours__title{font-family:'Lato',Arial,sans-serif;font-weight:900;font-size:15px;letter-spacing:.5px}
  .hours__rule{width:34px;height:3px;background:var(--pink);margin:6px auto 14px}
  .hours p{font-size:10.5px;line-height:1.45}
  .hours p + p{margin-top:10px}
  .contact-icons{display:flex;justify-content:center;gap:10px;margin:20px 0 16px}
  .contact-icons svg{width:24px;height:24px}
  .hours .contact-line{font-size:10.5px;line-height:1.75}

  .wordmark{display:flex;align-items:center;gap:8px;font-family:'Lato',Arial,sans-serif;
    font-weight:700;color:var(--purple);white-space:nowrap}
  .wordmark i{display:block;border-radius:50%;background:var(--purple)}

  .cover-title{font-family:'Lato',Arial,sans-serif;text-transform:uppercase;line-height:1}
  .cover-title strong{display:block;font-weight:900;font-size:38px;color:var(--purple);letter-spacing:1px}
  .cover-title em{display:block;font-style:normal;font-weight:300;font-size:46px;color:var(--pink);letter-spacing:1px;margin-top:2px}
  .pill{display:flex;align-items:center;justify-content:center;background:var(--purple);color:#fff;
    border-radius:20px;font-family:'Lato',Arial,sans-serif;font-size:13px;letter-spacing:1px}

  .service-cols{display:grid;grid-template-columns:1fr 1fr;column-gap:10px;margin-top:14px}
  .service{display:flex;gap:7px;align-items:flex-start;margin-bottom:14px}
  .service svg{flex:0 0 22px;width:22px;height:22px}
  .service h4{font-family:'Lato',Arial,sans-serif;font-weight:900;font-size:7.5px;color:var(--pink);text-transform:uppercase;line-height:1.3;padding-top:4px}
  .service small{display:block;font-family:'Open Sans',Arial,sans-serif;font-weight:400;font-size:7px;color:var(--grey);text-transform:none;line-height:1.3}

  .criteria{list-style:none;margin-top:8px}
  .criteria li{position:relative;padding-left:16px;font-size:7.6px;line-height:1.35;color:var(--grey);margin-bottom:7px}
  .criteria li::before{content:"";position:absolute;left:2px;top:1px;width:4px;height:7px;
    border-right:2px solid var(--purple);border-bottom:2px solid var(--purple);transform:rotate(40deg)}

  .step{position:absolute;width:98px;height:42px;display:flex;align-items:center;justify-content:center;
    text-align:center;padding:4px 6px;color:#fff;font-size:7px;line-height:1.25}
  .step--blue{background:var(--blue)}
  .step--teal{background:var(--teal)}
  .step--green{background:var(--green)}

  .call-pill{position:absolute;left:742px;top:690px;width:316px;height:28px;border-radius:14px;
    background:var(--purple);color:#fff;display:flex;align-items:center;justify-content:center;
    font-family:'Lato',Arial,sans-serif;font-size:11px;letter-spacing:.5px}
  .call-pill b{font-weight:900;margin-left:5px}
  .call-url{position:absolute;left:742px;top:726px;width:316px;text-align:center;font-size:8.5px;color:var(--pink);letter-spacing:.6px}
</style>
</head>
<body>

<section class="spread spread--outside">
  <svg class="layer" viewBox="0 0 1080 764" aria-hidden="true">
    <path d="M360 0 H720 V575 Q560 610 360 690 Z" fill="var(--purple)"/>
    <path d="M360 705 Q560 625 720 590" fill="none" stroke="var(--pink)" stroke-width="7"/>
    <path d="M360 722 Q560 642 720 607" fill="none" stroke="var(--purple)" stroke-width="8"/>
    <path d="M0 224 Q120 264 300 239 Q510 203 574 0" fill="none" stroke="var(--pink)" stroke-width="7"/>
    <path d="M0 240 Q120 280 300 255 Q520 215 592 0" fill="none" stroke="#ffffff" stroke-width="6"/>
    <path d="M0 252 Q120 292 300 267 Q530 225 604 0" fill="none" stroke="var(--purple)" stroke-width="9"/>
    <path d="M720 118 Q870 228 1080 220" fill="none" stroke="var(--pink)" stroke-width="10"/>
    <path d="M720 138 Q870 246 1080 238" fill="none" stroke="var(--purple)" stroke-width="8"/>
    <path d="M720 414 Q890 444 1080 514" fill="none" stroke="var(--purple)" stroke-width="9"/>
    <path d="M720 433 Q890 463 1080 533" fill="none" stroke="var(--pink)" stroke-width="8"/>
  </svg>
  <svg class="layer" viewBox="0 0 1080 764" role="img" aria-label="Photo of a smiling group of healthcare staff standing together">
    <defs><linearGradient id="teamTone" x1="0" y1="0" x2="1" y2="1">
      <stop offset="0" stop-color="#5b4038"/><stop offset=".5" stop-color="#c9a898"/><stop offset="1" stop-color="#e9e2e6"/>
    </linearGradient></defs>
    <path d="M0 0 H560 Q500 190 300 225 Q120 250 0 210 Z" fill="url(#teamTone)"/>
  </svg>
  <svg class="layer" viewBox="0 0 1080 764" role="img" aria-label="Photo of a carer sharing a high five with an elderly woman outdoors among green trees">
    <defs><linearGradient id="coverTone" x1="0" y1="0" x2="1" y2="1">
      <stop offset="0" stop-color="#7fae4a"/><stop offset=".55" stop-color="#c8d9a6"/><stop offset="1" stop-color="#7fa6cf"/>
    </linearGradient></defs>
    <path d="M720 150 Q870 258 1080 250 V500 Q890 430 720 400 Z" fill="url(#coverTone)"/>
  </svg>

  <div class="block" style="left:22px;top:272px;width:318px">
    <h2 class="heading"><b>About</b> <span>Us</span></h2>
    <p class="body-copy">Calm Fern Healthcare is a staffing provider with a contemporary approach to recruiting and placing skilled people in human services. We maintain a wide pool of registered nurses, enrolled nurses, support workers, cooks and cleaners across aged care, disability and community care.</p>
    <p class="body-copy">Our vision is to be the most responsive staffing agency in Australia.</p>
  </div>
  <div class="block" style="left:22px;top:378px;width:318px">
    <h2 class="heading"><b>Why Clients</b> <span>Choose Us</span></h2>
    <p class="body-copy">Calm Fern Healthcare partners with like-minded organisations with a passion for making a difference to the lives of the vulnerable. We have refined our recruitment so every placement is matched to the needs of your residents and clients, shift by shift.</p>
    <p class="body-copy">If you partner with us, we guarantee a tailored approach to meeting your needs.</p>
  </div>
  <div class="block" style="left:22px;top:490px;width:318px">
    <h2 class="heading"><b>Our Value</b> <span>Proposition</span></h2>
    <ul class="value-list value-list--pair">
      <li><span class="num">001.</span>Our people are individually selected and take part in robust recruitment processes</li>
      <li><span class="num">004.</span>We believe in ethical practices, transparency, and accountability</li>
      <li><span class="num">002.</span>We treat everyone with respect and believe our staff are the purpose of our existence</li>
      <li><span class="num">005.</span>We are deliberate in our approach and have a passion for human services</li>
      <li><span class="num">003.</span>We are responsive to our clients' priorities and walk along their journey</li>
      <li><span class="num">006.</span>We have a 'bias for action' and pursue every chance to adapt to our clients</li>
    </ul>
  </div>

  <div class="block hours" style="left:380px;top:244px;width:320px">
    <h3 class="hours__title">OFFICE HOURS</h3>
    <div class="hours__rule"></div>
    <p>Monday to Friday 8am- 6pm<br>Afterhours (Bookings Only)</p>
    <p>Monday-Friday 6pm-11pm/ 5am-8am;<br>Saturdays and Sunday (all hours)</p>
    <div class="contact-icons" aria-hidden="true">
      <svg viewBox="0 0 24 24"><circle cx="12" cy="12" r="11" fill="var(--pink)"/><path d="M12 6a4 4 0 0 0-4 4c0 3 4 8 4 8s4-5 4-8a4 4 0 0 0-4-4z" fill="#fff"/><circle cx="12" cy="10" r="1.5" fill="var(--pink)"/></svg>
      <svg viewBox="0 0 24 24"><circle cx="12" cy="12" r="11" fill="var(--pink)"/><rect x="6.5" y="8" width="11" height="8" fill="#fff"/><path d="M6.5 8 L12 12.5 L17.5 8" fill="none" stroke="var(--pink)" stroke-width="1.2"/></svg>
      <svg viewBox="0 0 24 24"><circle cx="12" cy="12" r="11" fill="var(--pink)"/><path d="M8.5 6.5l2 .3.8 3-1.4 1.2a8 8 0 0 0 3.1 3.1l1.2-1.4 3 .8.3 2a1.5 1.5 0 0 1-1.6 1.5A10 10 0 0 1 7 8.1 1.5 1.5 0 0 1 8.5 6.5z" fill="#fff"/></svg>
      <svg viewBox="0 0 24 24"><circle cx="12" cy="12" r="11" fill="var(--pink)"/><circle cx="12" cy="12" r="5.5" fill="none" stroke="#fff" stroke-width="1.2"/><ellipse cx="12" cy="12" rx="2.3" ry="5.5" fill="none" stroke="#fff" stroke-width="1"/><path d="M6.5 12h11" stroke="#fff" stroke-width="1"/></svg>
    </div>
    <p class="contact-line">18 Wattle Bend, Harlow WA 6190<br>admin@calmfernhealthcare.com.au<br>08 9000 4172<br>www.calmfernhealthcare.com.au</p>
  </div>
  <div class="block wordmark" style="left:420px;top:712px;font-size:17px">
    <i style="width:14px;height:14px"></i>Calm Fern Healthcare
  </div>

  <div class="block wordmark" style="left:760px;top:66px;font-size:24px">
    <i style="width:20px;height:20px"></i>Calm Fern Healthcare
  </div>
  <h1 class="block cover-title" style="left:748px;top:548px;width:320px">
    <strong>Reimagining</strong><em>Healthcare</em>
  </h1>
  <div class="block pill" style="left:748px;top:662px;width:308px;height:38px">www.calmfernhealthcare.com.au</div>
</section>

<section class="spread spread--inside">
  <svg class="layer" viewBox="0 0 1080 764" aria-hidden="true">
    <defs>
      <marker id="arrowHead" viewBox="0 0 6 6" refX="5" refY="3" markerWidth="5" markerHeight="5" orient="auto">
        <path d="M0 0 L6 3 L0 6 Z" fill="#9a95a0"/>
      </marker>
    </defs>
    <rect x="720" y="0" width="360" height="764" fill="var(--panel-tint)"/>
    <path d="M330 44 Q560 186 720 256 Q880 156 1080 96" fill="none" stroke="var(--pink)" stroke-width="9"/>
    <path d="M330 64 Q560 206 720 276 Q880 176 1080 116" fill="none" stroke="var(--purple)" stroke-width="8"/>
    <path d="M0 553 Q220 523 410 610" fill="none" stroke="var(--purple)" stroke-width="8"/>
    <path d="M0 571 Q220 541 404 626" fill="none" stroke="var(--pink)" stroke-width="7"/>
    <g stroke="#9a95a0" stroke-width="1.5" marker-end="url(#arrowHead)">
      <line x1="840" y1="541" x2="850" y2="541"/>
      <line x1="949" y1="541" x2="959" y2="541"/>
      <line x1="1009" y1="562" x2="1009" y2="573"/>
      <line x1="960" y1="595" x2="950" y2="595"/>
      <line x1="851" y1="595" x2="841" y2="595"/>
      <line x1="791" y1="616" x2="791" y2="627"/>
    </g>
  </svg>
  <svg class="layer" viewBox="0 0 1080 764" role="img" aria-label="Photo strip of carers spending time with elderly residents, playing cards and chatting outdoors">
    <defs><linearGradient id="stripTone" x1="0" y1="0" x2="1" y2="0">
      <stop offset="0" stop-color="#a8b6c4"/><stop offset=".5" stop-color="#d1a57f"/><stop offset="1" stop-color="#7f9c5a"/>
    </linearGradient></defs>
    <path d="M330 0 H1080 V80 Q880 140 720 240 Q560 170 330 30 Z" fill="url(#stripTone)"/>
  </svg>
  <svg class="layer" viewBox="0 0 1080 764" role="img" aria-label="Photo of a nurse walking arm in arm with a smiling elderly woman using a walker">
    <defs><linearGradient id="walkTone" x1="0" y1="0" x2="1" y2="1">
      <stop offset="0" stop-color="#d8cfc6"/><stop offset=".6" stop-color="#9c8c84"/><stop offset="1" stop-color="#efeff1"/>
    </linearGradient></defs>
    <path d="M0 586 Q220 556 400 640 V764 H0 Z" fill="url(#walkTone)"/>
  </svg>
  <svg class="layer" viewBox="0 0 1080 764" role="img" aria-label="Photo of a city skyline beside a river at dusk">
    <defs><linearGradient id="cityTone" x1="0" y1="0" x2="0" y2="1">
      <stop offset="0" stop-color="#9fb9d6"/><stop offset=".6" stop-color="#d9a66e"/><stop offset="1" stop-color="#3f5f6e"/>
    </linearGradient></defs>
    <path d="M560 764 V640 Q640 630 720 590 V764 Z" fill="url(#cityTone)"/>
  </svg>

  <div class="block" style="left:22px;top:30px;width:300px">
    <h2 class="heading"><b>Our</b> <span>Philosophy</span></h2>
    <p class="body-copy">Calm Fern Healthcare has a client focused approach which ensures it identifies individual client requirements to build a unique partnership without ambiguity. We look beyond staffing needs to understand the profile of the clients in your care, so that people with matching values arrive ready for every shift.</p>
    <p class="body-copy">Our staff retention programs focus on the key drivers for staff to perform their work well. With a proactive reward and recognition program, our people stay engaged, and the experience they build stays with the clients they support.</p>
  </div>
  <div class="block" style="left:22px;top:262px;width:320px">
    <h2 class="heading"><b>Our Value</b> <span>Proposition</span></h2>
    <ul class="value-list">
      <li><span class="num">001.</span>Our people are individually selected and participate in robust recruitment processes</li>
      <li><span class="num">002.</span>We treat everyone with respect and believe our staff are the purpose of our existence</li>
      <li><span class="num">003.</span>We are responsive to our clients priorities and walk along their journey to achieving operational excellence</li>
      <li><span class="num">004.</span>We believe in ethical practices, transparency, and accountability</li>
      <li><span class="num">005.</span>We are deliberate in our approach and have a passion for human services</li>
      <li><span class="num">006.</span>We have a 'bias for action' and unceasingly pursue opportunities to change and adapt to the needs of our clients and environment</li>
    </ul>
  </div>

  <div class="block" style="left:380px;top:282px;width:326px">
    <h2 class="heading"><b>Our</b> <span>Services</span></h2>
    <p class="body-copy">Our mission is to supply values driven, responsive, conscientious and reliable personnel to the aged care sector, disability services, private and public health sectors. Our passion for human services enables us to attract people with great values, ready to make a difference to the lives of vulnerable people.</p>
    <p class="body-copy">We have a comprehensive database of the following personnel:</p>
    <div class="service-cols">
      <div>
        <div class="service"><svg viewBox="0 0 22 22" aria-hidden="true"><circle cx="11" cy="11" r="10" fill="var(--pink)"/><path d="M9.5 6h3v3.5H16v3h-3.5V16h-3v-3.5H6v-3h3.5z" fill="#fff"/></svg><h4>Registered Nurses<small>(Aged Care, Disability, Emergency, Public and Private healthcare)</small></h4></div>
        <div class="service"><svg viewBox="0 0 22 22" aria-hidden="true"><circle cx="11" cy="11" r="10" fill="var(--pink)"/><rect x="6" y="8" width="10" height="7" rx="1" fill="#fff"/><rect x="9" y="6" width="4" height="2" fill="#fff"/></svg><h4>Clinical Nurses</h4></div>
        <div class="service"><svg viewBox="0 0 22 22" aria-hidden="true"><circle cx="11" cy="11" r="10" fill="var(--pink)"/><circle cx="11" cy="8.5" r="2.5" fill="#fff"/><path d="M6.5 16a4.5 4.5 0 0 1 9 0z" fill="#fff"/></svg><h4>Nurse Practitioners</h4></div>
        <div class="service"><svg viewBox="0 0 22 22" aria-hidden="true"><circle cx="11" cy="11" r="10" fill="var(--pink)"/><rect x="7" y="6" width="8" height="10" rx="1" fill="#fff"/><path d="M9 9h4M9 11.5h4M9 14h3" stroke="var(--pink)" stroke-width="1"/></svg><h4>Enrolled Nurses</h4></div>
        <div class="service"><svg viewBox="0 0 22 22" aria-hidden="true"><circle cx="11" cy="11" r="10" fill="var(--pink)"/><path d="M6 12h10a5 5 0 0 1-10 0z" fill="#fff"/><path d="M8 9.5h6" stroke="#fff" stroke-width="1.4"/></svg><h4>Kitchen Hands</h4></div>
      </div>
      <div>
        <div class="service"><svg viewBox="0 0 22 22" aria-hidden="true"><circle cx="11" cy="11" r="10" fill="var(--pink)"/><path d="M11 16s-5-3-5-6.3A2.7 2.7 0 0 1 11 8a2.7 2.7 0 0 1 5 1.7C16 13 11 16 11 16z" fill="#fff"/></svg><h4>Assistants in Nursing<small>(Carers/ PCA's)</small></h4></div>
        <div class="service"><svg viewBox="0 0 22 22" aria-hidden="true"><circle cx="11" cy="11" r="10" fill="var(--pink)"/><circle cx="8.5" cy="9" r="2" fill="#fff"/><circle cx="13.5" cy="9" r="2" fill="#fff"/><path d="M5 15.5a3.5 3.5 0 0 1 7 0zM10 15.5a3.5 3.5 0 0 1 7 0z" fill="#fff"/></svg><h4>Support Workers<small>(Disability, Community and Mental Health)</small></h4></div>
        <div class="service"><svg viewBox="0 0 22 22" aria-hidden="true"><circle cx="11" cy="11" r="10" fill="var(--pink)"/><rect x="7.5" y="10" width="7" height="5" fill="#fff"/><circle cx="9" cy="9" r="2" fill="#fff"/><circle cx="13" cy="9" r="2" fill="#fff"/></svg><h4>Healthcare Endorsed Chefs and Cooks</h4></div>
        <div class="service"><svg viewBox="0 0 22 22" aria-hidden="true"><circle cx="11" cy="11" r="10" fill="var(--pink)"/><path d="M8 6v10M14 6v3a2 2 0 0 1-2 2v5" stroke="#fff" stroke-width="1.6" fill="none"/></svg><h4>Catering Assistants</h4></div>
        <div class="service"><svg viewBox="0 0 22 22" aria-hidden="true"><circle cx="11" cy="11" r="10" fill="var(--pink)"/><path d="M8 8h6l-1 8H9z" fill="#fff"/><rect x="10" y="5.5" width="2" height="2.5" fill="#fff"/></svg><h4>Cleaners</h4></div>
      </div>
    </div>
  </div>

  <div class="block" style="left:742px;top:292px;width:318px">
    <h2 class="heading"><b>Working</b> <span>With Us</span></h2>
    <p class="body-copy" style="font-size:7.6px">All staff must meet the following benchmark criteria</p>
    <ul class="criteria">
      <li>9 months relevant industry experience in Australia</li>
      <li>National police clearance under 6 months old (must have unsupervised contact for vulnerable groups)</li>
      <li>Qualifications and registrations e.g. Certificate III Individual Support or AHPRA registration</li>
      <li>Excellent communication skills</li>
      <li>A genuine passion for people's health and wellbeing</li>
      <li>A reliable vehicle and state issued drivers licence</li>
      <li>An understanding of quality and safety outcomes for healthcare providers</li>
      <li>Flexibility and adaptability</li>
    </ul>
  </div>

  <div class="step step--blue" style="left:742px;top:520px">Expression of interest</div>
  <div class="step step--blue" style="left:851px;top:520px">Phone interview and initial suitability checks</div>
  <div class="step step--teal" style="left:960px;top:520px">Face to face interview</div>
  <div class="step step--teal" style="left:960px;top:574px">Reference checks, Compliance checks, Employment Assessments</div>
  <div class="step step--green" style="left:851px;top:574px">Conditional offer of employment extended</div>
  <div class="step step--green" style="left:742px;top:574px">Induction &amp; onboarding processes</div>
  <div class="step step--green" style="left:742px;top:628px">Final employment offer</div>

  <div class="call-pill">CALL US TODAY<b>08 9000 4172</b></div>
  <div class="call-url">www.calmfernhealthcare.com.au</div>
</section>

</body>
</html>
```